Technical Communications firm needs an article turned into a white paper

We want to redesign a 3-part blog series into a white paper that we can print for a conference. I've consolidated the three posts into the attached Word document.

We are looking for a light, easy to read design. Good use of graphics to support the message. I've added the graphics we used in the original post.

You can view them at
http://www.lanternquill.com/blog/are-you-satisfied-with-your-dita-solution/

Target Market(s)

Product managers from High-tech, Finance, and Medical industries.

Industry/Entity Type

Information Technology

Colors

Designer to choose colors to be used in the design.

Requirements
Must have
• Must be modern, light, easy to read and slick design. Try to incorporate the graphics provided, but feel free to add more. Must retain the lists and tables.
• Must align with our website/brand.
• Must be easy to read. So not too busy.
• Please move all footnotes to endnotes. You'll need to rework the numbering.
Nice to have
• Awesome coverpage.
Should not have
• Hokey clipart. Not too heavy or hard to read.

```html
<!DOCTYPE html>
<html lang="en">
<head>
<meta charset="utf-8">
<title>White Paper – Pages 5 and 6</title>
<link rel="stylesheet" href="https://fonts.googleapis.com/css2?family=Exo+2:ital,wght@0,400;0,600;0,700;1,400&display=swap">
<style>
  :root{
    --backdrop:#e9e6e1;
    --paper:#ffffff;
    --ink:#3a3f4a;
    --navy:#2e2f7f;
    --sky:#22a6dc;
    --note-bg:#e6e7ea;
    --faint:#ececec;
  }
  *{box-sizing:border-box;margin:0;padding:0}
  html,body{width:1200px;height:1200px;overflow:hidden;background:var(--backdrop);font-family:"Exo 2",sans-serif;color:var(--ink)}
  .page{position:absolute;top:243px;width:505px;height:714px;background:var(--paper);box-shadow:0 2px 8px rgba(0,0,0,.15);overflow:hidden}
  .page--five{left:68px}
  .page--six{left:627px}
  .page-label{position:absolute;top:985px;width:505px;text-align:center;font-size:22px;color:#555}
  .block{position:absolute;left:30px;width:445px;font-size:6.6px;line-height:9px;text-align:justify}
  .block p+p{margin-top:9px}
  .ref{color:var(--sky)}
  .list{position:absolute;left:30px;width:445px;list-style:none;font-size:6.6px}
  .list li{display:flex;align-items:center;height:17px}
  .list li::before{content:"";width:8px;height:8px;border-radius:50%;border:1.6px solid var(--sky);border-right-color:var(--navy);margin-right:8px;flex:none}
  .list--caps li{text-transform:uppercase}
  .inline-list{position:absolute;left:30px;width:445px;list-style:none;display:flex;font-size:6.6px}
  .inline-list li{display:flex;align-items:center}
  .inline-list li::before{content:"";width:8px;height:8px;border-radius:50%;border:1.6px solid var(--sky);border-right-color:var(--navy);margin-right:5px;flex:none}
  .inline-list li:nth-child(1){width:88px}
  .inline-list li:nth-child(2){width:94px}
  .inline-list li:nth-child(3){width:103px}
  .section-head{position:absolute;left:30px;height:32px;display:flex;align-items:center}
  .section-head svg{width:32px;height:32px;position:relative;z-index:2}
  .section-head h2{margin-left:-4px;background:var(--sky);color:#fff;font-size:9px;font-weight:700;letter-spacing:.2px;padding:3px 10px 3px 12px;border-radius:0 8px 8px 0;text-transform:uppercase}
  .footer-band{position:absolute;left:0;top:683px;width:505px;height:16px;background:var(--sky);color:#fff;font-size:7.5px;letter-spacing:3px;text-align:center;line-height:16px}
  .footer-rule{position:absolute;left:0;top:701px;width:505px;height:3px;background:var(--navy)}
  .page-number{position:absolute;left:456px;top:677px;width:29px;height:29px;border-radius:50%;background:#fff;border:3px solid var(--navy);font-size:9px;display:flex;align-items:center;justify-content:center;color:var(--navy)}
  .endnotes{position:absolute;left:0;top:570px;width:505px;height:113px;background:var(--note-bg)}
  .endnote{position:absolute;left:30px;width:445px;display:flex;font-size:6.4px;line-height:9px;font-style:italic}
  .endnote span:first-child{width:16px;color:var(--sky);flex:none}
  .faint-name{position:absolute;left:93px;top:282px;display:flex;align-items:center;gap:12px}
  .faint-name .dot{width:104px;height:104px;border-radius:50%;background:var(--faint)}
  .faint-name .word{font-size:30px;font-weight:700;color:var(--faint);line-height:30px;letter-spacing:.5px}
</style>
</head>
<body>

<section class="page page--five">
  <div class="block" style="top:32px">If the overall time and effort does not significantly improve over the course of 2–3 production life cycles of the content, then there may be some other issues at play. You'll want to examine your</div>
  <ul class="list" style="top:62px">
    <li>PROCESSES : Have you eliminated redundant activities in your processes?</li>
    <li>PIPES : Is your productivity impeded by network performance?</li>
    <li>Platforms : Are users experiencing problems related to disparate desktop configurations?</li>
    <li>Processors : Are your servers or client machines underpowered for the tools?</li>
    <li>People : Do your users follow established best practices for working with your tools?</li>
  </ul>
  <div class="block" style="top:166px">Once you've identified all external factors affecting performance, you'll want to examine how your tools are configured and deployed. There may be alternative features, configurations, or components that will greatly improve system performance. Your tool vendors or service providers should be able to help you examine your options.</div>

  <div class="section-head" style="top:211px">
    <svg viewBox="0 0 32 32" aria-hidden="true"><circle cx="16" cy="16" r="15" fill="#fff" stroke="var(--navy)" stroke-width="2"/><circle cx="16" cy="16" r="11" fill="none" stroke="#888" stroke-width="1"/><circle cx="16" cy="16" r="7" fill="none" stroke="#888" stroke-width="1"/><circle cx="16" cy="16" r="3" fill="none" stroke="#888" stroke-width="1"/></svg>
    <h2>Complexity Problems</h2>
  </div>
  <div class="block" style="top:254px">
    <p>Finding the correct balance of complexity versus utility is one of the biggest challenges we face in MODA deployments. The problem may not be that your tools are too complex, rather that too much complexity is exposed to the wrong group of users. The best-architected systems attempt to push the most complexity onto the shoulders of the fewest number of people. As much as possible, let the software handle most of the heavy lifting.</p>
    <p>It's important to note that collaborative, structured authoring is always going to be more complex than traditional desktop publishing. Despite attempts to simplify the technology around content authoring, content itself is not getting any simpler. Jonah Galt of Northwick Research believes that content development practices and technology are following trends we see in other related industries. His predictions are that content development will continue to become much more <span class="ref">[ii]</span></p>
  </div>
  <ul class="inline-list" style="top:357px">
    <li>Precise</li><li>Complex</li><li>Collaborative</li><li>Integrated into larger enterprise systems.</li>
  </ul>
  <div class="block" style="top:389px">To strike the proper balance between complexity and utility you need to consider how the technology decisions you make now impact the viability of your content in the future. Will simpler structures, semantics, and metadata cause significant rework in the future to attain your goals? Or, will postponing certain complexities increase the likelihood for adoption and pave the way for early wins? The only way to answer these questions is to map out your long-term goals and assess the steps you will take to get there.</div>

  <div class="section-head" style="top:439px">
    <svg viewBox="0 0 32 32" aria-hidden="true"><circle cx="16" cy="16" r="15" fill="#fff" stroke="var(--navy)" stroke-width="2"/><rect x="10" y="8" width="13" height="16" rx="1" fill="none" stroke="#555" stroke-width="1.2"/><circle cx="17" cy="14" r="2" fill="#555"/><path d="M13.5 21c0-3 7-3 7 0" fill="#555"/><path d="M8 11h3M8 15h3M8 19h3" stroke="#555" stroke-width="1"/></svg>
    <h2>Steps to Address Complexity</h2>
  </div>
  <div class="block" style="top:483px">
    <p>The first step to understanding your needs is to assess your level of process maturity against industry benchmarks. There are a few models to choose from including the Content Maturity Ladder <span class="ref">[iii]</span>. Once you've determined your current state, you can decide upon your timing to achieve your target state and map out the steps to get there.</p>
    <p>The second step is to develop a content strategy and roadmap that speak to your goals and capabilities you need to achieve over the next two years. Your strategy should align with your business goals and direction. Plan for a minor review every 6 months and a major review each year to determine your funding requirements to stay the course with your roadmap.</p>
    <p>By understanding your plan and getting sign-off from stakeholders, you will be able to determine whether you should</p>
  </div>
  <ul class="list list--caps" style="top:579px">
    <li>Eliminate certain elements that are unnecessarily complex</li>
    <li>Hire more staff to assume responsibility for some of the more complex tasks</li>
    <li>Invest more time and money in training to compensate for complexity</li>
    <li>Invest more money in tools that better mask the complexity, or</li>
    <li>Re-engineer certain aspects of your processes.</li>
  </ul>

  <div class="footer-band">www.lanternquill.com</div>
  <div class="footer-rule"></div>
  <div class="page-number">05</div>
</section>

<section class="page page--six">
  <div class="section-head" style="top:29px">
    <svg viewBox="0 0 32 32" aria-hidden="true"><circle cx="16" cy="16" r="15" fill="#fff" stroke="var(--navy)" stroke-width="2"/><circle cx="16" cy="16" r="11" fill="none" stroke="#888" stroke-width="1"/><circle cx="16" cy="16" r="7" fill="none" stroke="#888" stroke-width="1"/><circle cx="16" cy="16" r="3" fill="none" stroke="#888" stroke-width="1"/></svg>
    <h2>Lantern Quill Health Check</h2>
  </div>
  <div class="block" style="top:72px">Before making any moves to replace your current technology stack, let us work with you to assess your needs and review the current state of your deployment. We may be able to discover areas for improvement and extend the usefulness of your existing technology. If you need new tools, we can help you with that as well. Sometimes we all just need to stop throwing more technology at our content problems. Learn more about our workshops.</div>

  <div class="faint-name" aria-hidden="true">
    <div class="dot"></div>
    <div class="word">LANTERN<br>QUILL</div>
  </div>

  <div class="endnotes"></div>
  <div class="endnote" style="top:586px"><span>[i]</span><span>MODA Satisfaction Survey published by The Content Drover on May 31, 2017. Listen to an analysis of the results by Reid Hollis, Kevin Sandford-Ross, Martin Lowe, and Stuart Ames and download a copy of the results today from ClearCast at https://www.clearcast-demo.com/webcast/9273/259775</span></div>
  <div class="endnote" style="top:622px"><span>[ii]</span><span>Collaborating Across the Enterprise using MODA XML and Microcontent presented by Reid Hollis at StructCon North America 2017 in San Diego, CA.</span></div>
  <div class="endnote" style="top:649px"><span>[iii]</span><span>The Content Maturity Ladder Whitepaper by Miles Prentice and Alma Stowe, 2008<br>http://maturity-docs.org/wiki/about-the-content-maturity-ladder-</span></div>

  <div class="footer-band">www.lanternquill.com</div>
  <div class="footer-rule"></div>
  <div class="page-number">06</div>
</section>

<div class="page-label" style="left:68px">PAGE-5</div>
<div class="page-label" style="left:627px">PAGE-6</div>

</body>
</html>
```